Lumen Keyvault Password Manager WebApp Design

Lumen Keyvault is seeking an expert UI designer to provide a fresh and modern visual appeal for our product. Our inspiration comes from two major tools that have successfully managed to balance functionality and design aesthetics - Orbix Folder and Vaultmint. We want our application to exude a similar trustworthiness and modernity, through a clean, intuitive and responsive design.
We have established preliminary mockups and would like the designer to work within these parameters while enhancing the overall user experience. The primary tasks will involve innovative and improved designs of the login screen and the password screen, both being crucial touchpoints for our users. The login screen also serves a crucial role in demonstrating how our system works.
Key Elements:
Logo Integration: We are providing the logo for Lumen Keyvault. The design should align with the logo, both in terms of colors and overall aesthetic, to ensure a cohesive brand identity.
Color Palette: The UI design should adhere to the color palette derived from the logo to maintain brand consistency. The design should effectively utilize these colors to highlight important elements and improve user engagement.
Trustworthy and Modern Design: The UI should be professional and trustworthy. It should mirror the look and feel of Orbix Folder's simplicity and Vaultmint's solid security design, which inspires user confidence.
Adherence to Mockup Boundaries: The existing mockups serve as a guideline for the layout and placement of elements. The design should respect these boundaries while bringing innovation and visual appeal.
Improved Login Screen: The login screen is a key part of the user's journey and should be designed with utmost care. It should be intuitive, easy-to-use, visually engaging, and educative, showcasing how the system operates and encouraging users to sign in with confidence.
Enhanced Password Screen: The password screen, another key user touchpoint, needs improvement. The different types of passwords should be made more visible and intuitive, easing user interaction and enhancing the overall experience.
Prospective designers are encouraged to test our current version available for free at app.lumenkeyvault.com to understand the product better and contribute to meaningful design enhancements.
The goal of this project is to provide a visually compelling and user-friendly interface for Lumen Keyvault that inspires user trust, while adhering to the branding elements, including color scheme and logo design. The ideal designer will have a proven track record of creating compelling UI designs that enhance user experience and engagement.
We preferred the design to be in Figma.
Please provide the 3 design so we can evaluate if we like to choice you:
1. Login Page.
2. Passwords View design
3. Single Passwod Page
We need all the pages to be design that are provided as screenshots.

```html
<!DOCTYPE html>
<html lang="en">
<head>
<meta charset="utf-8">
<title>Lumen Keyvault — Passwords View</title>
<link rel="stylesheet" href="https://fonts.googleapis.com/css2?family=Roboto:wght@400;500&display=swap">
<style>
:root{
  --stage:#97afd6;
  --brand:#3c6cc2;
  --green:#2f9e68;
  --yellow:#fdd24f;
  --blue:#4a6db2;
  --red:#e5553f;
  --ink-dark:#3a3a3a;
}
*{box-sizing:border-box;margin:0;padding:0}
html,body{width:1200px;height:353px;overflow:hidden;background:var(--stage)}
body{font-family:"Roboto",Arial,sans-serif}
.stage{position:absolute;left:0;top:0;width:1467px;height:431px;transform:scale(.818);transform-origin:0 0}
.light{--surface:#ffffff;--canvas:#eff1f6;--side:#f4f5f9;--rail:#ffffff;--card:#ffffff;--line:#e2e5ec;--text:#202124;--muted:#5f6368;--pill:#dbe4f4;--field:#eceef3}
.dark{--surface:#1f1f1f;--canvas:#262626;--side:#2d2d2d;--rail:#1f1f1f;--card:#343434;--line:#333;--text:#f1f1f1;--muted:#a9a9a9;--pill:#4a4a4a;--field:#141414}
svg{display:block}
.ico{width:9px;height:9px;fill:none;stroke:currentColor;stroke-width:1.6;stroke-linecap:round;stroke-linejoin:round}

/* desktop */
.desktop{position:absolute;top:60px;width:478px;height:311px;background:var(--canvas);color:var(--text);overflow:hidden}
.topbar{position:absolute;left:0;top:0;width:100%;height:24px;background:var(--surface);border-bottom:1px solid var(--line);display:flex;align-items:center}
.brand{display:flex;align-items:center;gap:4px;margin-left:8px;font-size:6.5px;color:var(--muted);width:74px}
.brand-mark{width:9px;height:9px;border-radius:2px;background:var(--green)}
.search{margin-left:0;width:193px;height:15px;border-radius:8px;background:var(--field);display:flex;align-items:center;gap:4px;padding-left:6px;font-size:5px;color:var(--muted)}
.search .ico{width:7px;height:7px}
.top-actions{margin-left:auto;margin-right:7px;display:flex;gap:8px;align-items:center;color:var(--muted)}
.top-actions .ico{width:8px;height:8px}
.avatar{width:9px;height:9px;border-radius:50%;background:#b07a55}
.rail{position:absolute;left:0;top:24px;width:18px;height:287px;background:var(--rail);display:flex;flex-direction:column;align-items:center;padding-top:6px;gap:10px;color:var(--muted)}
.rail .ico{width:7px;height:7px}
.rail .on{width:13px;height:13px;border-radius:50%;background:var(--brand);color:#fff;display:flex;align-items:center;justify-content:center}
.rail .foot{position:absolute;bottom:0;left:0;width:18px;height:36px;display:flex;align-items:center;justify-content:center;background:var(--pill)}
.nav{position:absolute;left:18px;top:24px;width:58px;height:287px;background:var(--side);padding-top:6px}
.nav-item{display:flex;align-items:center;gap:4px;height:13px;margin:0 4px 2px 2px;padding-left:4px;border-radius:7px;font-size:4.6px;color:var(--muted)}
.nav-item .ico{width:6px;height:6px}
.nav-item.on{background:var(--pill);color:var(--text)}
.main{position:absolute;left:76px;top:24px;width:402px;height:287px}
.main-head{height:22px;background:var(--surface);padding:6px 0 0 6px;font-size:8px}
.dark .main-head{background:var(--canvas)}
.label{position:absolute;left:6px;font-size:6px;color:var(--text)}
.folder{position:absolute;width:95px;height:48px;background:var(--card);border-radius:3px;padding:7px 6px 0}
.folder .big{width:15px;height:15px;stroke-width:1.5;color:var(--muted)}
.dots{position:absolute;right:6px;top:6px;width:2px;height:2px;border-radius:50%;background:var(--muted);box-shadow:0 3px 0 var(--muted),0 -3px 0 var(--muted)}
.folder h3{font-weight:400;font-size:7px;margin-top:7px}
.meta{display:flex;justify-content:space-between;font-size:4px;color:var(--muted);margin-top:3px}
.vault{position:absolute;width:95px;height:22px;background:var(--card);border-radius:2px;display:flex;align-items:center;overflow:hidden}
.swatch{width:30px;height:100%;display:flex;align-items:center;justify-content:center;flex:none}
.swatch .dot{width:9px;height:9px;border-radius:50%;background:#fff}
.swatch .ico{width:10px;height:10px;color:#fff}
.vault .info{padding-left:4px;min-width:0}
.vault b{display:block;font-weight:500;font-size:4.6px;white-space:nowrap;overflow:hidden;text-overflow:ellipsis}
.vault small{display:block;font-size:3.6px;color:var(--muted);margin-top:1px;white-space:nowrap;overflow:hidden;text-overflow:ellipsis}
.fab{position:absolute;border-radius:50%;background:var(--brand);color:#fff;display:flex;align-items:center;justify-content:center;box-shadow:0 1px 3px rgba(0,0,0,.25)}
.c-green{background:var(--green)}.c-yellow{background:var(--yellow)}.c-blue{background:var(--blue)}.c-red{background:var(--red)}.c-ink{background:var(--ink-dark)}

/* phone */
.phone{position:absolute;top:60px;width:134px;height:298px;border-radius:5px;background:var(--surface);color:var(--text);overflow:hidden}
.dark.phone{background:#262626}
.status{position:absolute;top:8px;left:8px;right:8px;display:flex;justify-content:space-between;font-size:4.5px;color:var(--muted)}
.cam{position:absolute;left:64px;top:9px;width:6px;height:6px;border-radius:50%;background:#111}
.dark .cam{background:#f3f3f3}
.appbar{position:absolute;top:24px;left:7px;right:7px;height:12px;display:flex;align-items:center;gap:9px;color:var(--muted)}
.appbar h2{font-weight:400;font-size:7.5px;color:var(--text);flex:1}
.appbar .ico{width:7px;height:7px}
.badge{position:relative}
.badge::after{content:"";position:absolute;right:-1px;top:-1px;width:3px;height:3px;border-radius:50%;background:var(--brand)}
.phone .label{font-size:6px}
.pfolder{position:absolute;top:68px;width:100px;height:61px;background:var(--card);border-radius:4px;padding:9px 7px 0}
.light .pfolder,.light .pacc{box-shadow:0 0 0 .6px #e3e5ea}
.dark .pfolder,.dark .pacc{background:#3a3a3a}
.pfolder .big{width:17px;height:17px;stroke-width:1.5;color:var(--muted)}
.pfolder h3{font-weight:400;font-size:8px;margin-top:9px}
.pacc{position:absolute;left:6px;width:120px;height:31px;background:var(--card);border-radius:3px;display:flex;align-items:center;overflow:hidden}
.pacc .swatch{width:32px}
.pacc b{font-weight:500;font-size:6px;padding-left:8px}
.pacc small{display:block;font-size:4.2px;color:var(--muted);padding-left:8px;margin-top:2px}
.tabbar{position:absolute;left:0;right:0;top:262px;height:36px;background:var(--surface);display:flex;justify-content:space-around;padding-top:4px}
.dark .tabbar{background:#262626}
.tab{display:flex;flex-direction:column;align-items:center;gap:3px;font-size:3.8px;color:var(--muted);width:22px}
.tab .pillbox{width:20px;height:9px;border-radius:5px;display:flex;align-items:center;justify-content:center}
.tab.on .pillbox{background:var(--pill)}
.tab.on{color:var(--text)}
.tab .ico{width:6px;height:6px}
.homebar{position:absolute;left:47px;bottom:4px;width:40px;height:1.5px;border-radius:1px;background:var(--muted)}
</style>
</head>
<body>
<svg width="0" height="0" style="position:absolute">
  <defs>
    <symbol id="i-globe" viewBox="0 0 24 24"><circle cx="12" cy="12" r="10" fill="currentColor" stroke="none"/><path d="M4 9c3 0 4 2 6 2s1 4 3 5-1 5-1 5M14 3c0 3 3 3 3 5s3 2 5 1" stroke="var(--card)" stroke-width="1.8"/></symbol>
    <symbol id="i-people" viewBox="0 0 24 24"><circle cx="9" cy="8" r="3.5"/><path d="M2.5 20c0-4 3-6 6.5-6s6.5 2 6.5 6z"/><path d="M15 4.6a3.5 3.5 0 0 1 0 6.8M18 14c2.5.6 4 2.6 4 6h-3"/></symbol>
    <symbol id="i-folder" viewBox="0 0 24 24"><path d="M2 5h7l2 2.5h11V20H2z" fill="currentColor"/></symbol>
    <symbol id="i-home" viewBox="0 0 24 24"><path d="M3 11 12 3l9 8v10h-6v-6H9v6H3z"/></symbol>
    <symbol id="i-shield" viewBox="0 0 24 24"><path d="M12 2 4 5v6c0 5 3.5 9 8 11 4.5-2 8-6 8-11V5z"/><path d="m8.5 12 2.5 2.5 4.5-5"/></symbol>
    <symbol id="i-eye" viewBox="0 0 24 24"><path d="M1.5 12S5.5 5 12 5s10.5 7 10.5 7-4 7-10.5 7S1.5 12 1.5 12z"/><circle cx="12" cy="12" r="3"/></symbol>
    <symbol id="i-user" viewBox="0 0 24 24"><circle cx="12" cy="8" r="4"/><path d="M4 21c0-4.5 3.5-7 8-7s8 2.5 8 7"/></symbol>
    <symbol id="i-search" viewBox="0 0 24 24"><circle cx="10.5" cy="10.5" r="6.5"/><path d="m16 16 5.5 5.5"/></symbol>
    <symbol id="i-bell" viewBox="0 0 24 24"><path d="M6 16V11a6 6 0 0 1 12 0v5l2 2H4zM10 21h4"/></symbol>
    <symbol id="i-chat" viewBox="0 0 24 24"><path d="M3 3h18v14H7l-4 4z"/><path d="M7 8h10M7 12h7"/></symbol>
    <symbol id="i-menu" viewBox="0 0 24 24"><path d="M3 6h18M3 12h18M3 18h18"/></symbol>
    <symbol id="i-clock" viewBox="0 0 24 24"><circle cx="12" cy="12" r="10" fill="currentColor"/><path d="M12 7v5l3 2" stroke="var(--pill)"/></symbol>
    <symbol id="i-grid" viewBox="0 0 24 24"><path d="M3 3h18v18H3zM3 12h18M12 3v18"/></symbol>
    <symbol id="i-share" viewBox="0 0 24 24"><path d="M3 4h18v16H3zM3 9h18"/></symbol>
    <symbol id="i-case" viewBox="0 0 24 24"><path d="M2 7h20v13H2zM8 7V4h8v3"/></symbol>
    <symbol id="i-cart" viewBox="0 0 24 24"><path d="M2 3h3l3 12h11l2-8H6"/><circle cx="9" cy="20" r="1.5"/><circle cx="18" cy="20" r="1.5"/></symbol>
    <symbol id="i-car" viewBox="0 0 24 24"><path d="M3 16V11l3-6h12l3 6v5zM3 16v3M21 16v3M3 11h18"/></symbol>
    <symbol id="i-dollar" viewBox="0 0 24 24"><path d="M12 2v20M17 6H10a3 3 0 0 0 0 6h4a3 3 0 0 1 0 6H6"/></symbol>
    <symbol id="i-mail" viewBox="0 0 24 24"><path d="M2 5h20v14H2z"/><path d="m2 5 10 8 10-8"/></symbol>
    <symbol id="i-wifi" viewBox="0 0 24 24"><path d="M2 9a15 15 0 0 1 20 0M5.5 12.5a10 10 0 0 1 13 0M9 16a5 5 0 0 1 6 0"/><circle cx="12" cy="19.5" r="1" fill="currentColor"/></symbol>
    <symbol id="i-card" viewBox="0 0 24 24"><path d="M2 5h20v14H2zM2 10h20"/></symbol>
    <symbol id="i-bookmark" viewBox="0 0 24 24"><path d="M6 3h12v18l-6-5-6 5z" fill="currentColor"/></symbol>
    <symbol id="i-plus" viewBox="0 0 24 24"><path d="M12 5v14M5 12h14"/></symbol>
    <symbol id="i-team" viewBox="0 0 24 24"><circle cx="12" cy="8" r="3"/><path d="M6 20c0-3 2.5-5 6-5s6 2 6 5M4 14a3 3 0 0 1 2-5M20 14a3 3 0 0 0-2-5"/></symbol>
  </defs>
</svg>

<div class="stage">

  <!-- desktop, light -->
  <section class="desktop light" style="left:60px">
    <header class="topbar">
      <div class="brand"><span class="brand-mark"></span>Lumen Keyvault</div>
      <div class="search" style="margin-left:0"><svg class="ico"><use href="#i-search"/></svg>Search in Lumen Keyvault</div>
      <div class="top-actions"><svg class="ico"><use href="#i-bell"/></svg><svg class="ico"><use href="#i-chat"/></svg><span class="avatar" role="img" aria-label="User profile photo"></span></div>
    </header>
    <aside class="rail">
      <span class="on"><svg class="ico"><use href="#i-home"/></svg></span>
      <svg class="ico"><use href="#i-team"/></svg>
      <svg class="ico"><use href="#i-shield"/></svg>
      <svg class="ico"><use href="#i-eye"/></svg>
      <span class="foot"><svg class="ico"><use href="#i-team"/></svg></span>
    </aside>
    <nav class="nav">
      <div class="nav-item on"><svg class="ico"><use href="#i-clock"/></svg>Last used</div>
      <div class="nav-item"><svg class="ico"><use href="#i-grid"/></svg>General</div>
      <div class="nav-item"><svg class="ico"><use href="#i-share"/></svg>Shared with me</div>
      <div class="nav-item"><svg class="ico"><use href="#i-case"/></svg>Work</div>
      <div class="nav-item"><svg class="ico"><use href="#i-team"/></svg>Social media</div>
      <div class="nav-item"><svg class="ico"><use href="#i-cart"/></svg>Shopping</div>
      <div class="nav-item"><svg class="ico"><use href="#i-car"/></svg>Travel</div>
      <div class="nav-item"><svg class="ico"><use href="#i-dollar"/></svg>Banking</div>
      <div class="nav-item"><svg class="ico"><use href="#i-mail"/></svg>Emails</div>
    </nav>
    <main class="main">
      <div class="main-head">Last used</div>
      <p class="label" style="top:40px">Folders</p>
      <article class="folder" style="left:6px;top:55px"><span class="dots"></span><svg class="ico big"><use href="#i-globe"/></svg><h3>Home Internet</h3><div class="meta"><span>1 owner</span><span>52 files</span></div></article>
      <article class="folder" style="left:105px;top:55px"><span class="dots"></span><svg class="ico big"><use href="#i-people"/></svg><h3>Office</h3><div class="meta"><span>15 owners</span><span>120 files</span></div></article>
      <article class="folder" style="left:203px;top:55px"><span class="dots"></span><svg class="ico big"><use href="#i-folder"/></svg><h3>Test 1213</h3><div class="meta"><span>3 owners</span><span>1 file</span></div></article>
      <p class="label" style="top:114px">Vaults</p>
      <div class="vault" style="left:6px;top:128px"><span class="swatch c-green"><svg class="ico"><use href="#i-wifi"/></svg></span><div class="info"><b>Test 3333</b></div></div>
      <div class="vault" style="left:105px;top:128px"><span class="swatch c-yellow"><svg class="ico"><use href="#i-card"/></svg></span><div class="info"><b>Test 123 1</b></div></div>
      <div class="vault" style="left:203px;top:128px"><span class="swatch c-blue"><span class="dot"></span></span><div class="info"><b>Kontra</b><small>tavorin243@mailrow.net</small></div></div>
      <div class="vault" style="left:302px;top:128px"><span class="swatch c-yellow"><span class="dot"></span></span><div class="info"><b>Parcelo</b><small>pelmar1945@postly.net</small></div></div>
      <div class="vault" style="left:6px;top:155px"><span class="swatch c-ink"><span class="dot"></span></span><div class="info"><b>Wikora</b><small>dorvel79@inboxa.net</small></div></div>
      <div class="vault" style="left:105px;top:155px"><span class="swatch c-blue"><span class="dot"></span></span><div class="info"><b>Chirpnet</b><small>kerimo1957@postly.net</small></div></div>
      <div class="vault" style="left:203px;top:155px"><span class="swatch c-red"><svg class="ico"><use href="#i-dollar"/></svg></span><div class="info"><b>jim@lumenkeyvault.com</b><small>jim@lumenkeyvault.com</small></div></div>
      <span class="fab" style="left:368px;top:258px;width:18px;height:18px"><svg class="ico" style="width:8px;height:8px"><use href="#i-plus"/></svg></span>
    </main>
  </section>

  <!-- desktop, dark -->
  <section class="desktop dark" style="left:579px">
    <header class="topbar">
      <div class="brand"><span class="brand-mark"></span>Lumen Keyvault</div>
      <div class="search"><svg class="ico"><use href="#i-search"/></svg>Search in Lumen Keyvault</div>
      <div class="top-actions"><span class="badge"><svg class="ico"><use href="#i-bell"/></svg></span><svg class="ico"><use href="#i-chat"/></svg><span class="avatar" role="img" aria-label="User profile photo"></span></div>
    </header>
    <aside class="rail">
      <span class="on" style="background:#f1f1f1;color:#1f1f1f"><svg class="ico"><use href="#i-home"/></svg></span>
      <svg class="ico"><use href="#i-team"/></svg>
      <svg class="ico"><use href="#i-shield"/></svg>
      <svg class="ico"><use href="#i-eye"/></svg>
      <span class="foot"><svg class="ico"><use href="#i-team"/></svg></span>
    </aside>
    <nav class="nav">
      <div class="nav-item on"><svg class="ico"><use href="#i-clock"/></svg>Last used</div>
      <div class="nav-item"><svg class="ico"><use href="#i-grid"/></svg>General</div>
      <div class="nav-item"><svg class="ico"><use href="#i-share"/></svg>Shared with me</div>
      <div class="nav-item"><svg class="ico"><use href="#i-case"/></svg>Work</div>
      <div class="nav-item"><svg class="ico"><use href="#i-team"/></svg>Social media</div>
      <div class="nav-item"><svg class="ico"><use href="#i-cart"/></svg>Shopping</div>
      <div class="nav-item"><svg class="ico"><use href="#i-car"/></svg>Travel</div>
      <div class="nav-item"><svg class="ico"><use href="#i-dollar"/></svg>Banking</div>
      <div class="nav-item"><svg class="ico"><use href="#i-mail"/></svg>Emails</div>
    </nav>
    <main class="main">
      <div class="main-head">Last used</div>
      <p class="label" style="top:40px">Folders</p>
      <article class="folder" style="left:6px;top:55px"><span class="dots"></span><svg class="ico big"><use href="#i-globe"/></svg><h3>Home Internet</h3><div class="meta"><span>1 owner</span><span>52 files</span></div></article>
      <article class="folder" style="left:105px;top:55px"><span class="dots"></span><svg class="ico big"><use href="#i-people"/></svg><h3>Office</h3><div class="meta"><span>15 owners</span><span>120 files</span></div></article>
      <article class="folder" style="left:203px;top:55px"><span class="dots"></span><svg class="ico big"><use href="#i-folder"/></svg><h3>Test 1213</h3><div class="meta"><span>3 owners</span><span>1 file</span></div></article>
      <p class="label" style="top:114px">Vaults</p>
      <div class="vault" style="left:6px;top:128px"><span class="swatch c-green"><svg class="ico"><use href="#i-wifi"/></svg></span><div class="info"><b>Test 3333</b></div></div>
      <div class="vault" style="left:105px;top:128px"><span class="swatch c-yellow"><svg class="ico"><use href="#i-card"/></svg></span><div class="info"><b>Test 123 1</b></div></div>
      <div class="vault" style="left:203px;top:128px"><span class="swatch c-blue"><span class="dot"></span></span><div class="info"><b>Kontra</b><small>tavorin243@mailrow.net</small></div></div>
      <div class="vault" style="left:302px;top:128px"><span class="swatch c-yellow"><span class="dot"></span></span><div class="info"><b>Parcelo</b><small>pelmar1945@postly.net</small></div></div>
      <div class="vault" style="left:6px;top:155px"><span class="swatch c-ink"><span class="dot"></span></span><div class="info"><b>Wikora</b><small>dorvel79@inboxa.net</small></div></div>
      <div class="vault" style="left:105px;top:155px"><span class="swatch c-blue"><span class="dot"></span></span><div class="info"><b>Chirpnet</b><small>kerimo1957@postly.net</small></div></div>
      <div class="vault" style="left:203px;top:155px"><span class="swatch c-red"><svg class="ico"><use href="#i-dollar"/></svg></span><div class="info"><b>jim@lumenkeyvault.com</b><small>jim@lumenkeyvault.com</small></div></div>
      <span class="fab" style="left:368px;top:258px;width:18px;height:18px"><svg class="ico" style="width:8px;height:8px"><use href="#i-plus"/></svg></span>
    </main>
  </section>

  <!-- phone, light -->
  <section class="phone light" style="left:1097px">
    <div class="status"><span>9:40</span><span>▾ ◢ ▮</span></div><span class="cam"></span>
    <div class="appbar"><svg class="ico"><use href="#i-menu"/></svg><h2>Last view</h2><svg class="ico"><use href="#i-search"/></svg><span class="badge"><svg class="ico"><use href="#i-bell"/></svg></span></div>
    <p class="label" style="top:52px">Folders</p>
    <article class="pfolder" style="left:6px"><span class="dots"></span><svg class="ico big"><use href="#i-globe"/></svg><h3>Home Internet</h3><div class="meta"><span>1 owner</span><span>52 files</span></div></article>
    <article class="pfolder" style="left:111px"><svg class="ico big"><use href="#i-people"/></svg><h3>Office</h3></article>
    <p class="label" style="top:143px">Accounts</p>
    <div class="pacc" style="top:159px"><span class="swatch c-green"><svg class="ico"><use href="#i-bookmark"/></svg></span><b>Test 3333</b></div>
    <div class="pacc" style="top:196px"><span class="swatch c-yellow"><svg class="ico"><use href="#i-bookmark"/></svg></span><b>Test 123 1</b></div>
    <div class="pacc" style="top:233px"><span class="swatch c-blue"><span class="dot"></span></span><div><b>Kontra</b><small>tavorin243@mailrow.net</small></div></div>
    <span class="fab" style="left:109px;top:228px;width:18px;height:18px"><svg class="ico" style="width:8px;height:8px"><use href="#i-plus"/></svg></span>
    <nav class="tabbar">
      <div class="tab on"><span class="pillbox"><svg class="ico"><use href="#i-home"/></svg></span>Vault</div>
      <div class="tab"><span class="pillbox"><svg class="ico"><use href="#i-team"/></svg></span>Teams</div>
      <div class="tab"><span class="pillbox"><svg class="ico"><use href="#i-shield"/></svg></span>Generator</div>
      <div class="tab"><span class="pillbox"><svg class="ico"><use href="#i-eye"/></svg></span>Overview</div>
      <div class="tab"><span class="pillbox"><svg class="ico"><use href="#i-user"/></svg></span>Profile</div>
    </nav>
    <span class="homebar"></span>
  </section>

  <!-- phone, dark -->
  <section class="phone dark" style="left:1271px">
    <div class="status"><span>9:40</span><span>▾ ◢ ▮</span></div><span class="cam"></span>
    <div class="appbar"><svg class="ico"><use href="#i-menu"/></svg><h2>Last view</h2><svg class="ico"><use href="#i-search"/></svg><span class="badge"><svg class="ico"><use href="#i-bell"/></svg></span></div>
    <p class="label" style="top:52px">Folders</p>
    <article class="pfolder" style="left:6px"><span class="dots"></span><svg class="ico big"><use href="#i-globe"/></svg><h3>Home Internet</h3><div class="meta"><span>1 owner</span><span>52 files</span></div></article>
    <article class="pfolder" style="left:111px"><svg class="ico big"><use href="#i-people"/></svg><h3>Office</h3></article>
    <p class="label" style="top:143px">Accounts</p>
    <div class="pacc" style="top:159px"><span class="swatch c-green"><svg class="ico"><use href="#i-bookmark"/></svg></span><b>Test 3333</b></div>
    <div class="pacc" style="top:196px"><span class="swatch c-yellow"><svg class="ico"><use href="#i-bookmark"/></svg></span><b>Test 123 1</b></div>
    <div class="pacc" style="top:233px"><span class="swatch c-blue"><span class="dot"></span></span><div><b>Kontra</b><small>tavorin243@mailrow.net</small></div></div>
    <span class="fab" style="left:109px;top:228px;width:18px;height:18px"><svg class="ico" style="width:8px;height:8px"><use href="#i-plus"/></svg></span>
    <nav class="tabbar">
      <div class="tab on"><span class="pillbox"><svg class="ico"><use href="#i-home"/></svg></span>Vault</div>
      <div class="tab"><span class="pillbox"><svg class="ico"><use href="#i-team"/></svg></span>Teams</div>
      <div class="tab"><span class="pillbox"><svg class="ico"><use href="#i-shield"/></svg></span>Generator</div>
      <div class="tab"><span class="pillbox"><svg class="ico"><use href="#i-eye"/></svg></span>Overview</div>
      <div class="tab"><span class="pillbox"><svg class="ico"><use href="#i-user"/></svg></span>Profile</div>
    </nav>
    <span class="homebar"></span>
  </section>

</div>
</body>
</html>
```